Template design for micro site for a corporate-branded mobile software product

We need a creative web designer to help us quickly design a template design for a micro site webpage for a product called Korvane Unified Alerts, and we need the template design to be shown in 3 distinct industry designs. The template design shall be a one-page corporate brochure and product page, and the same template design will be re-used for 3 different industry pages. Although the layout and navigation design shall not change, each of the 3 industry pages must have its own unique design/content/look/feel to address specific capabilities of our product that are important to that industry or topic.

NOTE: This is a design project, not a web development project. We will hand your designs over to a web developer.

REQUIRED:
Create a template design that includes Korvane branding guidelines and can be used consistently for each of our 3 different industry micro site web pages (i.e., the template design should consider such things as overall page navigation design & layout design to deliver a common experience for the viewer).

REQUIRED:
In terms of layout, please model your template design after one of the following responsive website layouts, and please indicate which you chose:

http://www.plinththemes.example/gym-fitness-business-wordpress-theme-vigor/
http://www.plinththemes.example/meld-a-sleek-flashy-and-professional-wordpress-theme/
http://www.plinththemes.example/bold-and-modern-responsive-business-wordpress-theme-sprightly/
http://www.plinththemes.example/summit-business-premium-wordpress-theme/
http://themevault.example/themes/tailorix
http://www.plinththemes.example/level-kit-business-portfolio-wordpress-theme/
http://www.plinththemes.example/stillwater-premium-origin-child-theme/

REQUIRED:
Use the template to design 3 unique designs, one for each of the following 3 industry topic pages (you may change anything in the design such as colors, pictures, icons, etc. to create a look/feel relevant for the topic):
- Workplace Harassment & HR
- Financial Institutions
- Mining & Construction (includes Oil, Gas, etc.)

Attached are content ideas for the above 3 industry topics for use in your suggested designs.

REQUIRED: Korvane branding is a requirement (we must use the spectrum design element at top of page). Colors can (probably should) change for each of the 3 micro site designs. You can see examples of Korvane branding at www.korvane.example, www.korvane-kua.example/school, and in the attached PowerPoints.

REQUIRED: We must have a contact us form similar to the form at the bottom of www.korvane-kua.example/school or at the bottom of www.artguild.example. The specific goal of these 3 website designs are to drive sales leads and conversions to request more information from our sales team, so we are seeking a design/layout that helps drive site conversions.

REQUIRED: Navigation menu similar to the one at www.korvane.example (at the top of the page)

Nice to have:

PICTURES: Pictures will definitely need to change for each site. If you can make suggestions on pictures, that will help. We are ok with taking additional (optional) proposals if you find pictures you think really help the site.

Reason: We are looking for a design that really takes the Korvane branding guidelines into careful consideration.

We invite you to design your template based on one of the following responsive layouts, and please indicate to us which one you chose (so we can purchase it and give it to our web developer). Thank you.

Target Market(s)

Each of the 3 industry pages should target each of the following (respectively):
1. Workplace Harassment (general topic)
2. Financial Institutions (Banking, Insurance, Investment, Retail/Corporate)
3. Mining (includes Oil, Gas, and peripherally includes Energy)

See attached PowerPoint file for some content ideas for your design.

Industry/Entity Type

Software

Requirements
Must have
• - Templatte design must be modeled after one of the following layouts

- Template design must be a single page layout. Content should fit into screens of 1366x768, and no "scrolling" should be necessary if the user presses the navigation menu buttons (e.g., see www.korvane-kua.example/school for an example of how the navigation menu takes you to the content without scrolling)
- Each of the 3 micro site industry pages must be different (pictures, content, etc.) but must use the same template design
- Must use Korvane branding guidelines (attached)
- Must include a Contact Us form similar to the bottom of the page at www.korvane-kua.example/school or the bottom of the page at www.artguild.example
- Must include a Navigation Bar at the top similar to www.korvane.example
- Must maintain some consistency (visually and navigation) with existing 2 micro sites already launched (see URLs above)
Nice to have
• - Pictures (it is ok to send a separate proposal for pictures if cost is a concern)
- Visual appeal with professional and modern look/feel
- Consideration for driving site conversions to "Getting Started" and "Request More Info" buttons
- Consideration for responsive web developer
- Consideration for SEO
Should not have
• - Search box

```html
<!DOCTYPE html>
<html lang="en">
<head>
<meta charset="utf-8">
<title>Korvane Unified Alerts – Financial Institutions</title>
<link href="https://fonts.googleapis.com/css2?family=Open+Sans:wght@400;600;700;800&display=swap" rel="stylesheet">
<style>
:root{
  --navy:#0b1f3f;
  --nav-bg:#0e1a2e;
  --blue:#0a6fc2;
  --blue-bright:#1a8fe0;
  --blue-deep:#0b4f96;
  --sky:#d6e7f3;
  --text:#2c3440;
  --muted:#5b6572;
  --panel:#e7eaee;
  --field:#50565f;
  --white:#ffffff;
}
*{box-sizing:border-box;margin:0;padding:0}
html,body{width:783px;height:1200px;overflow:hidden}
body{font-family:"Open Sans",Arial,sans-serif;color:var(--text);background:var(--white);position:relative}

.top-nav{height:28px;background:var(--nav-bg);display:flex;align-items:stretch;padding-left:40px}
.top-nav a{color:#c9d3e0;font-size:8.5px;text-decoration:none;padding:0 14px;display:flex;align-items:center;border-right:1px solid #26334a}
.top-nav a.active{background:var(--blue);color:var(--white);font-weight:600}

.hero{position:relative;height:492px;overflow:hidden}
.hero-photo{position:absolute;inset:0;background:linear-gradient(100deg,#eef5fb 0%,#cfe2f1 38%,#b9d4ea 62%,#e3eef7 100%)}
.hero-figure{position:absolute;right:70px;top:30px;width:270px;height:420px;background:radial-gradient(ellipse at 50% 40%,#d9c3ae 0%,#b89a82 35%,rgba(120,110,110,.35) 70%,rgba(0,0,0,0) 72%)}
.hero-card{position:absolute;left:70px;top:150px;width:268px;padding:16px 18px 18px;background:rgba(11,79,150,.88);color:var(--white);border-radius:4px}
.hero-card .kicker{font-size:12px;font-weight:400}
.hero-card h1{font-size:20px;font-weight:800;letter-spacing:.3px;margin:2px 0 10px}
.hero-card p{font-size:8px;line-height:1.55;color:#e3eefa}
.hero-swoosh{position:absolute;left:0;bottom:0;width:783px;height:110px}

.features{display:flex;justify-content:space-between;padding:12px 40px 0;height:290px}
.feature{width:162px}
.feature .icon{width:58px;height:58px;border-radius:50%;background:var(--blue-deep);display:flex;align-items:center;justify-content:center;margin-bottom:12px}
.feature h3{font-size:11px;font-weight:700;color:var(--blue-deep);line-height:1.3;margin-bottom:8px;min-height:29px}
.feature ul{list-style:none}
.feature li{font-size:7.6px;line-height:1.45;color:var(--muted);padding-left:9px;position:relative;margin-bottom:3px}
.feature li::before{content:"";position:absolute;left:0;top:4px;width:4px;height:4px;background:var(--blue);border-radius:50%}

.integrate{position:absolute;left:0;top:810px;width:783px;height:355px;background:var(--panel);padding-top:28px}
.integrate h2{text-align:center;font-size:26px;font-weight:800;color:var(--navy);letter-spacing:.5px;margin-bottom:26px}
.integrate-body{display:flex;padding-left:115px;gap:78px}
.contact-form{width:235px;display:flex;flex-direction:column;gap:8px}
.contact-form .field{height:28px;background:var(--field);color:#e6e9ed;font-size:8.5px;padding:0 10px;display:flex;align-items:center}
.contact-form .or{font-size:8px;color:var(--muted);padding-left:4px;margin:-3px 0}
.contact-form .submit{width:88px;height:28px;background:var(--blue-bright);color:var(--white);font-weight:700;font-size:11px;border:none;margin-top:6px;font-family:inherit}
.integrate-info h4{font-size:9.5px;font-weight:700;color:var(--navy);margin-bottom:6px}
.integrate-info ul{list-style:none;margin-bottom:16px}
.integrate-info li{font-size:8px;line-height:1.6;color:var(--text);padding-left:9px;position:relative}
.integrate-info li::before{content:"";position:absolute;left:0;top:5px;width:4px;height:4px;background:var(--navy);border-radius:50%}

.site-footer{position:absolute;left:0;top:1165px;width:783px;height:35px;background:var(--nav-bg);display:flex;align-items:center;justify-content:center;gap:26px}
.footer-brand{display:flex;align-items:center;gap:6px;color:var(--white);font-size:8px;font-weight:600}
.footer-brand .mark{width:12px;height:12px;background:var(--blue-bright)}
.site-footer small{font-size:7px;color:#9aa6b6}
</style>
</head>
<body>

<nav class="top-nav">
  <a href="#">Korvane Home</a>
  <a href="#">Workplace Harassment</a>
  <a href="#" class="active">Financial Institutions</a>
  <a href="#">Mining &amp; Construction</a>
</nav>

<header class="hero">
  <div class="hero-photo" role="img" aria-label="Bright office background with a smiling businesswoman in a suit"></div>
  <div class="hero-figure" role="img" aria-label="Businesswoman portrait"></div>
  <div class="hero-card">
    <div class="kicker">Mobile Messaging Solution for</div>
    <h1>FINANCIAL INSTITUTIONS</h1>
    <p>KUA for Financial Institutions is a high-availability mobile messaging solution used for high-volume SMS at a number of financial systems. Built on the Korvane Unified Alerts platform and designed to integrate with mission critical and existing ecommerce systems to automate communication.</p>
  </div>
  <svg class="hero-swoosh" viewBox="0 0 783 110" preserveAspectRatio="none" aria-hidden="true">
    <path d="M0 70 C200 20 480 30 783 10 L783 110 L0 110 Z" fill="#1a8fe0" opacity=".55"/>
    <path d="M0 80 C220 40 500 55 783 30 L783 110 L0 110 Z" fill="#0a6fc2"/>
    <path d="M0 92 C250 62 520 78 783 58 L783 110 L0 110 Z" fill="#0b4f96"/>
    <path d="M0 100 C260 80 540 95 783 82 L783 110 L0 110 Z" fill="#ffffff"/>
  </svg>
</header>

<section class="features">
  <article class="feature">
    <div class="icon">
      <svg width="30" height="30" viewBox="0 0 30 30" fill="#fff" aria-hidden="true"><circle cx="10" cy="9" r="4"/><circle cx="20" cy="9" r="4"/><path d="M2 24c0-5 4-8 8-8s8 3 8 8z"/><path d="M14 24c0-4 3-8 6-8 4 0 8 3 8 8z" opacity=".8"/></svg>
    </div>
    <h3>Staff Fulfillment for Satellite Branches</h3>
    <ul>
      <li>Use SMS to automatically fulfil temporary and rostering shifts</li>
      <li>Send automatic mobile staff offers using "first to respond" method</li>
      <li>Integrate SMS into existing HR and rostering systems or processes</li>
      <li>Deploy as a hierarchical, single or multi-site implementation</li>
    </ul>
  </article>
  <article class="feature">
    <div class="icon">
      <svg width="30" height="30" viewBox="0 0 30 30" fill="none" stroke="#fff" stroke-width="2.2" aria-hidden="true"><rect x="4" y="6" width="22" height="14" rx="1.5"/><path d="M11 25h8M15 20v5"/></svg>
    </div>
    <h3>Account Services &amp; Customer Support</h3>
    <ul>
      <li>Keep an audit trail with full archival of all SMS conversations</li>
      <li>Send automatic SMS reminders for payments due or late payments</li>
      <li>Alert account holders via SMS of important account information</li>
      <li>Use URLs in SMS to link to web pages with detailed or private info</li>
      <li>Invite customers via SMS to update their current contact information</li>
    </ul>
  </article>
  <article class="feature">
    <div class="icon">
      <svg width="30" height="30" viewBox="0 0 30 30" fill="#fff" aria-hidden="true"><path d="M15 26 4 15a6 6 0 0 1 11-8 6 6 0 0 1 11 8z"/></svg>
    </div>
    <h3>Customer Loyalty</h3>
    <ul>
      <li>Integrate with existing CRM systems</li>
      <li>Use SMS programs for personal relationships with account holders</li>
      <li>Create opt-in SMS programs, mobile coupons and discount offers, such as "1st" new product announcements and "first to renew" promotions</li>
      <li>Allow customers to update their own contact information via SMS</li>
    </ul>
  </article>
  <article class="feature">
    <div class="icon">
      <svg width="30" height="30" viewBox="0 0 30 30" aria-hidden="true"><path d="M10 13V9a5 5 0 0 1 10 0v4" fill="none" stroke="#fff" stroke-width="2.4"/><rect x="7" y="13" width="16" height="12" rx="2" fill="#fff"/></svg>
    </div>
    <h3>Login Authentication Using SMS as 2nd Factor</h3>
    <ul>
      <li>Validate identity of internal and customer account holders</li>
      <li>Delivers one-time passwords via SMS to handsets</li>
      <li>Integrates seamlessly with existing online and ecommerce systems</li>
      <li>Eliminates the needs for physical hardware tokens</li>
    </ul>
  </article>
</section>

<section class="integrate">
  <h2>READY TO INTEGRATE?</h2>
  <div class="integrate-body">
    <form class="contact-form">
      <div class="field">Your Name*</div>
      <div class="field">Your Email</div>
      <div class="or">or</div>
      <div class="field">Your Phone#</div>
      <button type="button" class="submit">SUBMIT</button>
    </form>
    <div class="integrate-info">
      <h4>Custom &amp; Proprietary Systems Integration</h4>
      <ul>
        <li>APIs include HTTP/S, SMTP, SOAP, XML, SMPP, JSON, .NET</li>
      </ul>
      <h4>Comprehensive Solutions</h4>
      <ul>
        <li>Provider mobile messaging platform for financial institutions</li>
        <li>Integrated 2-way SMS, MMS, Email</li>
        <li>Highly configurable</li>
        <li>Setup Assistance</li>
        <li>Ready to use in 10 days</li>
        <li>Support 24x7x365</li>
      </ul>
    </div>
  </div>
</section>

<footer class="site-footer">
  <div class="footer-brand"><span class="mark"></span>Korvane Unified Alerts</div>
  <small>© 2013 Korvane Corp Pty Ltd. All rights reserved.</small>
</footer>

</body>
</html>
```